Birch Harbor - Countertop fabricator
Need stationary, business card and T-shirt design
Birch Harbor - Countertop fabricator -
Creative Brief
Simple
Kevin Rasble
14 Larkwood Lane Syracuse, NY13099
info@birchharborny.example
www.birchharborny.example
Back of card to list materials; Granite Quatz Marble Soapstone Solid Surface

```html
<!DOCTYPE html>
<html lang="en">
<head>
<meta charset="utf-8">
<title>Birch Harbor – Stationery Set</title>
<link href="https://fonts.googleapis.com/css2?family=Tinos:wght@400;700&display=swap" rel="stylesheet">
<style>
  :root {
    --brown: #6b4a25;
    --brown-dark: #4c3117;
    --brown-light: #8a6238;
    --tan: #c7ad8a;
    --paper: #ffffff;
    --frame: #c9c9c9;
    --edge: #d8d8d8;
    --ink: #5b4630;
    --window: #e4e4e4;
  }
  * { margin: 0; padding: 0; box-sizing: border-box; }
  html, body { width: 1200px; height: 852px; overflow: hidden; background: var(--paper); }
  body { position: relative; font-family: "Tinos", "Times New Roman", serif; color: var(--ink); }
  address { font-style: normal; }

  .sheet-frame {
    position: absolute; left: 8px; top: 8px; width: 1184px; height: 836px;
    border: 2px solid var(--frame); border-radius: 14px;
  }
  .piece { position: absolute; background: var(--paper); border: 1px solid var(--edge); overflow: hidden; }

  .brand { display: flex; flex-direction: column; align-items: flex-end; position: absolute; }
  .brand-mark { background: var(--brown); }
  .brand-name { font-weight: 400; color: var(--brown-dark); white-space: nowrap; }

  /* flat area standing in for the column ornament */
  .column-area {
    position: absolute;
    background: linear-gradient(90deg, var(--brown-dark), var(--brown) 50%, var(--brown-dark));
  }

  /* letterhead */
  .letterhead { left: 29px; top: 36px; width: 560px; height: 776px; }
  .letterhead .column-area { left: 14px; top: 0; width: 78px; height: 776px; }
  .letterhead .brand { right: 24px; top: 36px; }
  .letterhead .brand-mark { width: 54px; height: 48px; margin-right: 4px; }
  .letterhead .brand-name { font-size: 27px; margin-top: 10px; }
  .letterhead-address {
    position: absolute; right: 24px; bottom: 22px; text-align: right;
    font-size: 13px; line-height: 18px;
  }

  /* business card front */
  .card-front { left: 612px; top: 36px; width: 228px; height: 168px; }
  .card-front .column-area { right: 8px; top: 0; width: 26px; height: 168px; }
  .card-front .brand { left: 16px; top: 10px; align-items: flex-start; }
  .card-front .brand-mark { width: 22px; height: 20px; }
  .card-front .brand-name { font-size: 11px; margin-top: 3px; }
  .card-name {
    position: absolute; left: 0; width: 194px; top: 62px; text-align: center;
    font-size: 17px; font-weight: 700; color: var(--brown);
  }
  .card-contact {
    position: absolute; left: 14px; top: 112px; width: 176px;
    font-size: 5.5px; line-height: 8px; white-space: nowrap;
  }

  /* business card back */
  .card-back {
    left: 859px; top: 132px; width: 226px; height: 137px; border: none;
    background: linear-gradient(135deg, var(--brown-light), var(--brown-dark));
    box-shadow: 2px 2px 4px rgba(0,0,0,0.25);
  }
  .card-back .brand { left: 0; right: 0; top: 18px; align-items: center; }
  .card-back .brand-mark { width: 44px; height: 40px; background: var(--tan); }
  .card-back .brand-name { color: #fff; font-size: 17px; margin-top: 6px; }
  .card-materials {
    position: absolute; left: 0; right: 0; top: 102px; text-align: center;
    color: #f0e3cf; font-size: 7.5px; letter-spacing: 0.3px;
  }

  /* envelope front */
  .envelope { left: 612px; top: 283px; width: 540px; height: 250px; }
  .envelope .column-area { left: 4px; top: 0; width: 70px; height: 250px; }
  .envelope .brand { right: 22px; top: 10px; }
  .envelope .brand-mark { width: 46px; height: 40px; margin-right: 4px; }
  .envelope .brand-name { font-size: 20px; margin-top: 6px; }
  .envelope-window {
    position: absolute; left: 150px; top: 104px; width: 208px; height: 52px;
    background: var(--window); border: 1px solid #d2d2d2; border-radius: 8px;
  }
  .envelope-address {
    position: absolute; right: 16px; top: 206px; text-align: right;
    font-size: 8px; line-height: 11px; white-space: nowrap;
  }

  /* envelope back */
  .envelope-back { left: 612px; top: 552px; width: 540px; height: 252px; }
  .envelope-flap { position: absolute; left: 0; top: 0; }
  .envelope-back .brand { left: 0; right: 0; top: 8px; align-items: center; }
  .envelope-back .brand-mark { width: 26px; height: 24px; background: var(--tan); }
</style>
</head>
<body>
  <div class="sheet-frame"></div>

  <section class="piece letterhead">
    <div class="column-area" role="img" aria-label="Decorative brown column ornament running down the left edge"></div>
    <div class="brand">
      <div class="brand-mark"></div>
      <div class="brand-name">BirchHarbor</div>
    </div>
    <address class="letterhead-address">
      14 Larkwood Lane Syracuse, NY13099<br>
      Phone : 315-555-0142 ; Cell : 315-555-0187 ; Fax : 607-555-0123<br>
      Email : info@birchharborny.example ; www.birchharborny.example
    </address>
  </section>

  <section class="piece card-front">
    <div class="column-area" role="img" aria-label="Decorative brown column ornament along the right edge"></div>
    <div class="brand">
      <div class="brand-mark"></div>
      <div class="brand-name">BirchHarbor</div>
    </div>
    <div class="card-name">Kevin Rasble</div>
    <address class="card-contact">
      14 Larkwood Lane Syracuse, NY13099<br>
      Phone : 315-555-0142 ; Cell : 315-555-0187 ; Fax : 607-555-0123<br>
      Email : info@birchharborny.example ; www.birchharborny.example
    </address>
  </section>

  <section class="piece card-back">
    <div class="brand">
      <div class="brand-mark"></div>
      <div class="brand-name">BirchHarbor</div>
    </div>
    <div class="card-materials">Granite | Quartz | Marble | Soapstone | Solid Surface</div>
  </section>

  <section class="piece envelope">
    <div class="column-area" role="img" aria-label="Decorative brown column ornament at the left edge"></div>
    <div class="brand">
      <div class="brand-mark"></div>
      <div class="brand-name">BirchHarbor</div>
    </div>
    <div class="envelope-window"></div>
    <address class="envelope-address">
      14 Larkwood Lane Syracuse, NY13099<br>
      Phone : 315-555-0142 ; Cell : 315-555-0187 ; Fax : 607-555-0123<br>
      Email : info@birchharborny.example ; www.birchharborny.example
    </address>
  </section>

  <section class="piece envelope-back">
    <svg class="envelope-flap" width="540" height="90" viewBox="0 0 540 90">
      <path d="M0 0 H540 V40 Q540 72 500 72 H40 Q0 72 0 40 Z" fill="var(--brown)"/>
    </svg>
    <div class="brand">
      <div class="brand-mark"></div>
    </div>
  </section>
</body>
</html>
```